Rear Window Advertisement and Magnets for side doors

Questions about Solvanta insurance?
Ask me, I'm a nurse
629-###-####
(Disclaimer.................in small print....)

```html
<!DOCTYPE html>
<html lang="en">
<head>
<meta charset="utf-8">
<title>Solvanta Insurance Door Magnet</title>
<link rel="stylesheet" href="https://fonts.googleapis.com/css2?family=Oswald:wght@500;600&display=swap">
<style>
  :root {
    --canvas-bg: #ffffff;
    --magnet-teal: #2da0a8;
    --magnet-teal-deep: #238c95;
    --headline-white: #ffffff;
    --headline-navy: #2c3f8f;
    --photo-scrubs: #3a6f9a;
    --photo-shadow: #1f4766;
    --art-scrubs: #4fa59a;
    --art-outline: #2e6f6a;
  }
  * { box-sizing: border-box; margin: 0; padding: 0; }
  html, body {
    width: 1200px;
    height: 1200px;
    overflow: hidden;
    background: var(--canvas-bg);
  }
  .canvas {
    width: 1200px;
    height: 1200px;
    display: flex;
    flex-direction: column;
    align-items: center;
    justify-content: center;
    gap: 40px;
  }
  .door-magnet {
    position: relative;
    width: 900px;
    height: 545px;
    background: linear-gradient(135deg, var(--magnet-teal) 0%, var(--magnet-teal-deep) 100%);
    display: flex;
    overflow: hidden;
  }
  .nurse-visual {
    width: 42%;
    height: 100%;
    flex-shrink: 0;
  }
  .nurse-visual--photo {
    background: linear-gradient(160deg, var(--photo-scrubs) 0%, var(--photo-shadow) 100%);
  }
  .nurse-visual--illustration {
    background: linear-gradient(160deg, var(--art-scrubs) 0%, var(--art-outline) 100%);
  }
  .message {
    flex: 1;
    padding: 30px 30px 0 18px;
    font-family: "Oswald", "Arial Narrow", sans-serif;
    font-weight: 600;
    text-transform: uppercase;
    line-height: 1.05;
  }
  .message__question {
    font-size: 62px;
    color: var(--headline-white);
  }
  .message__topic {
    font-size: 62px;
    color: var(--headline-navy);
  }
  .message__nurse {
    margin-top: 10px;
    font-size: 46px;
    font-weight: 500;
    color: var(--headline-white);
  }
  .message__phone {
    margin-top: 4px;
    font-size: 72px;
    color: var(--headline-white);
    letter-spacing: 1px;
  }
</style>
</head>
<body>
  <main class="canvas">
    <section class="door-magnet door-magnet--photo">
      <div class="nurse-visual nurse-visual--photo" role="img" aria-label="Photo of a nurse in blue scrubs with a stethoscope, arms crossed"></div>
      <div class="message">
        <p class="message__question">Questions<br>about</p>
        <p class="message__topic">Solvanta<br>insurance?</p>
        <p class="message__nurse">Ask me, I'm a nurse</p>
        <p class="message__phone">629-###-####</p>
      </div>
    </section>

    <section class="door-magnet door-magnet--illustration">
      <div class="nurse-visual nurse-visual--illustration" role="img" aria-label="Illustration of a nurse in green scrubs and surgical cap, arms crossed"></div>
      <div class="message">
        <p class="message__question">Questions<br>about</p>
        <p class="message__topic">Solvanta<br>insurance?</p>
        <p class="message__nurse">Ask me, I'm a nurse</p>
        <p class="message__phone">629-###-####</p>
      </div>
    </section>
  </main>
</body>
</html>
```